Heritage Hollow Business Cards

Require a business card design. <br/><br/>Needs to include logo (either round or long version) plus these details:<br/>Maya Torvel<br/>Heritage Hollow<br/>maya@quonbrook.com.au<br/>02 6481 7390<br/>PO Box Glenwarra NSW 2913<br/>www.heritagehollow.com.au<br/><br/>I need in an editable format so that I can create for multiple staff members. <br/><br/>

Target Market(s)

We are an online store selling renovation products to home owners are builders. Looking for a classic classy design.

Industry/Entity Type

Home And Garden

Contact Information for Business Card

Maya Torvel
Heritage Hollow
maya@quonbrook.com.au
02 6481 7390
PO Box Glenwarra NSW 2913
www.heritagehollow.com.au

Colors

Designer to choose colors to be used in the design.

Requirements
Must have
• Must include Logo.

```html
<!DOCTYPE html>
<html lang="en">
<head>
<meta charset="utf-8">
<title>Heritage Hollow Business Cards</title>
<link href="https://fonts.googleapis.com/css2?family=Josefin+Slab:wght@400;600&display=swap" rel="stylesheet">
<style>
  :root {
    --backdrop: #8e8e8e;
    --card-white: #ffffff;
    --card-black: #2b2b2b;
    --ink: #1b1b1b;
    --ink-soft: #8a8a8a;
    --line-white: #f2f2f2;
    --sketch-tone: #e6e6e6;
  }
  * { box-sizing: border-box; margin: 0; padding: 0; }
  html, body {
    width: 1200px; height: 960px; overflow: hidden;
    background: var(--backdrop);
    font-family: "Josefin Slab", Georgia, serif;
  }
  .card {
    position: absolute; left: 272px;
    width: 655px; height: 373px; overflow: hidden;
  }
  .card--front { top: 59px; background: var(--card-white); color: var(--ink); }
  .card--back { top: 501px; background: var(--card-black); }

  .person-name {
    position: absolute; left: 74px; top: 70px;
    font-size: 26px; font-weight: 600; letter-spacing: 0.5px; text-transform: uppercase;
  }
  .person-role { position: absolute; left: 74px; top: 104px; font-size: 18px; color: var(--ink-soft); }
  .company-name { position: absolute; left: 74px; top: 138px; font-size: 17px; }
  .company-address { position: absolute; left: 74px; top: 162px; font-size: 17px; color: var(--ink-soft); letter-spacing: 0.3px; }
  .contact-list { position: absolute; left: 74px; top: 192px; list-style: none; }
  .contact-item {
    display: flex; align-items: center; gap: 8px;
    height: 24px; font-size: 16.5px; color: var(--ink-soft);
  }
  .contact-item:first-child { font-size: 18px; }
  .contact-icon { width: 13px; height: 13px; flex: none; }

  .roof-sketch { position: absolute; left: 356px; top: 188px; }

  .brand-mark { position: absolute; left: 220px; top: 64px; width: 226px; height: 226px; }
  .brand-name {
    position: absolute; left: 220px; top: 64px; width: 226px; height: 226px;
    display: flex; flex-direction: column; justify-content: center; align-items: center;
    padding-top: 90px;
    color: var(--line-white); font-size: 32px; font-weight: 600; line-height: 1;
    text-align: center;
  }
</style>
</head>
<body>

<section class="card card--front">
  <h1 class="person-name">Maya Torvel</h1>
  <p class="person-role">Founder &amp; CEO</p>
  <p class="company-name">Heritage Hollow</p>
  <p class="company-address">PO Box Glenwarra NSW 2913</p>
  <ul class="contact-list">
    <li class="contact-item">
      <svg class="contact-icon" viewBox="0 0 16 16"><path d="M4 1l3 3-2 2c1 2 3 4 5 5l2-2 3 3-2 3C7 15 1 9 1 3z" fill="#1b1b1b"/></svg>
      02 6481 7390
    </li>
    <li class="contact-item">
      <svg class="contact-icon" viewBox="0 0 16 16"><rect x="1" y="3" width="14" height="10" fill="#1b1b1b"/><path d="M1 3l7 6 7-6" fill="none" stroke="#fff" stroke-width="1.2"/></svg>
      maya@quonbrook.com.au
    </li>
    <li class="contact-item">
      <svg class="contact-icon" viewBox="0 0 16 16" fill="none" stroke="#1b1b1b" stroke-width="1.3"><circle cx="8" cy="8" r="6.5"/><ellipse cx="8" cy="8" rx="3" ry="6.5"/><path d="M1.5 8h13M2.5 4.5h11M2.5 11.5h11"/></svg>
      www.heritagehollow.com.au
    </li>
  </ul>
  <svg class="roof-sketch" width="310" height="190" viewBox="0 0 310 190" role="img" aria-label="Hand-sketched house roof gable inside a circle">
    <circle cx="152" cy="152" r="152" fill="var(--sketch-tone)"/>
  </svg>
</section>

<section class="card card--back">
  <svg class="brand-mark" viewBox="0 0 226 226">
    <circle cx="113" cy="113" r="112" fill="none" stroke="var(--line-white)" stroke-width="1.5"/>
  </svg>
  <div class="brand-name"><span>Heritage</span><span>Hollow</span></div>
</section>

</body>
</html>
```